Flex Forward Thaw 21 day Challenge

We are having a Flex Forward Thaw Challenge at our fitness studio. We need a poster design using the template attached as a reference. I have also included our Molvaro logo to put on the poster. Please DO NOT use the graphics in the flyer as we are expecting something much better :-)

-Size needed 11x17 with bleeding for printing

-We need this made in Photoshop (CS3 friendly) or at least delivered in PS as we might change some text or re-arrange the design later on.

-We need this in layers.

```html
<!DOCTYPE html>
<html lang="en">
<head>
<meta charset="utf-8">
<title>Flex Forward Thaw 21 day Challenge</title>
<link rel="stylesheet" href="https://fonts.googleapis.com/css2?family=Questrial&family=Didact+Gothic&family=Open+Sans:wght@400&family=Oswald:wght@600&display=swap">
<style>
  :root {
    --sky-top: #a9cdea;
    --sky-mid: #d9e8f3;
    --horizon: #b8b2a6;
    --road: #4a4d52;
    --road-deep: #2f3236;
    --title-red: #e8321e;
    --title-orange: #f46a1c;
    --copy-orange: #f07424;
    --copy-amber: #f39a1e;
    --silver: #e9edf0;
    --ink: #26282b;
    --brand-blue: #3d8fd4;
    --white: #ffffff;
    --quote-bg: rgba(40, 42, 46, 0.72);
    --footer-yellow: #ffb21c;
  }
  * { margin: 0; padding: 0; box-sizing: border-box; }
  html, body { width: 777px; height: 1200px; overflow: hidden; background: var(--white); }
  .poster {
    position: relative;
    width: 777px;
    height: 1200px;
    overflow: hidden;
    font-family: "Questrial", sans-serif;
  }
  .backdrop {
    position: absolute;
    inset: 0;
    background: linear-gradient(180deg,
      var(--sky-top) 0%,
      var(--sky-mid) 45%,
      var(--horizon) 58%,
      var(--road) 70%,
      var(--road-deep) 100%);
  }
  .brand {
    position: absolute;
    left: 34px;
    top: 60px;
    display: flex;
    align-items: center;
    gap: 14px;
  }
  .brand-mark {
    width: 34px;
    height: 34px;
    background: var(--brand-blue);
  }
  .brand-name {
    font-family: "Questrial", sans-serif;
    font-size: 66px;
    color: var(--ink);
    letter-spacing: 2px;
  }
  .headline {
    position: absolute;
    left: 0;
    width: 100%;
    text-align: center;
    font-family: "Didact Gothic", sans-serif;
    line-height: 1;
    -webkit-text-stroke: 1.5px var(--white);
    text-shadow: 0 3px 4px rgba(0,0,0,0.35);
  }
  .headline-top { top: 290px; font-size: 82px; padding-left: 60px; }
  .headline-bottom { top: 382px; font-size: 100px; }
  .word-hot { color: var(--title-red); }
  .word-bright { color: var(--title-orange); }
  .word-silver { color: var(--silver); -webkit-text-stroke: 1.5px #9aa3aa; }
  .copy {
    position: absolute;
    left: 0;
    width: 100%;
    text-align: center;
    color: var(--copy-orange);
    text-shadow: 0 0 3px var(--white), 0 0 6px rgba(255,255,255,0.8);
    line-height: 1.32;
  }
  .lead { top: 490px; font-size: 35px; color: var(--title-red); line-height: 1.27; }
  .perk { font-size: 25px; }
  .perk-sessions { top: 602px; color: var(--copy-amber); }
  .perk-nutrition { top: 698px; color: var(--copy-amber); }
  .perk-plan { top: 795px; color: var(--copy-amber); }
  .perk-coach { top: 892px; color: var(--copy-orange); }
  .offer { top: 978px; font-size: 28px; color: var(--title-red); }
  .offer-price { font-size: 38px; }
  .testimonial {
    position: absolute;
    left: 26px;
    top: 1032px;
    width: 712px;
    height: 94px;
    background: var(--quote-bg);
    color: var(--white);
    font-family: "Open Sans", sans-serif;
    font-size: 19px;
    line-height: 1.37;
    text-align: center;
    padding-top: 6px;
  }
  .call-to-action {
    position: absolute;
    right: 12px;
    top: 1138px;
    text-align: right;
    font-family: "Oswald", sans-serif;
    font-weight: 600;
    font-size: 17px;
    line-height: 1.4;
    color: var(--footer-yellow);
    -webkit-text-stroke: 0.6px #e0461a;
    text-transform: uppercase;
  }
</style>
</head>
<body>
  <main class="poster">
    <div class="backdrop" role="img" aria-label="Photo of a runner's legs striding down an open desert highway under a bright cloudy blue sky"></div>

    <div class="brand">
      <span class="brand-mark"></span>
      <span class="brand-name">Molvaro</span>
    </div>

    <h1>
      <span class="headline headline-top"><span class="word-hot">FLEX</span> <span class="word-silver">FORWARD</span></span>
      <span class="headline headline-bottom"><span class="word-bright">THAW</span></span>
    </h1>

    <p class="copy lead">Discover the Secret to a<br>Beach-Ready Body in Just 21 Days!</p>

    <p class="copy perk perk-sessions">9 total training sessions designed to incinerate fat<br>off your midsection, thighs, and arms</p>
    <p class="copy perk perk-nutrition">21 days of nutritional guidance<br>including delicious recipes</p>
    <p class="copy perk perk-plan">A Success Session to map out your<br>individual plan for success</p>
    <p class="copy perk perk-coach">Your very own Personal Accountability Coach<br>to ensure you get results</p>

    <p class="copy offer">You get all this—a $399 value—for <span class="offer-price">ONLY $99!</span></p>

    <blockquote class="testimonial">
      Insert Testimonial<br>
      I’ve never been more fit in my life—at age 41!<br>
      ~Marla Penhurst
    </blockquote>

    <p class="call-to-action">Hurry! Space is limited to only 20 participants!!!<br>Claim your spot now: website and phone number</p>
  </main>
</body>
</html>
```